Sena & Kaan Wedding Invitation and Decorative Designs

We are looking for a sweet and elegant design for our wedding invitation. We need different versions of the same design to use both as printed hard copies and in digital formats (WhatsApp image, instagram post, etc) Please see attached sample invitation, which we like as a simple and elegant option, but also find it quite basic. We are open to creative suggestions following a similar style.
Once we decide on an invitation design, we would like to use the same design elements in guest name cards, welcome sign, menu cards and print cover for the dance floor of our wedding venue. Please see random samples of these materials attached. We also attach a photo from our wedding venue displaying a close to final visual of the decoration we chose for our wedding day (sharing in case it helps as an inspiration source and helps with matching decoration colors with the designs)
- Must have a style similar to the attached sample invitation

```html
<!DOCTYPE html>
<html lang="tr">
<head>
<meta charset="utf-8">
<title>Sena &amp; Kaan – Düğün Davetiyesi</title>
<link rel="stylesheet" href="https://fonts.googleapis.com/css2?family=Cinzel:wght@400;700&family=Great+Vibes&display=swap">
<style>
  :root{
    --page:#f4f1f3;
    --gold:#bf9a3c;
    --gold-deep:#a8832a;
    --gold-light:#e9cf78;
    --wash-pink:#f1d6e6;
    --wash-blue:#c9d9ec;
    --wash-lilac:#e4dcef;
    --petal-pink:#e06a9c;
    --petal-violet:#c46ad0;
    --leaf:#7fae6a;
  }
  *{margin:0;padding:0;box-sizing:border-box}
  html,body{width:1200px;height:1200px;overflow:hidden}
  body{background:var(--page);position:relative;font-family:"Cinzel",serif;color:var(--gold)}

  .invitation{
    position:absolute;left:220px;top:60px;width:760px;height:1080px;overflow:hidden;
    background:
      radial-gradient(ellipse at 70% 12%, var(--wash-blue) 0%, transparent 45%),
      radial-gradient(ellipse at 20% 55%, var(--wash-pink) 0%, transparent 55%),
      radial-gradient(ellipse at 80% 85%, var(--wash-pink) 0%, transparent 50%),
      radial-gradient(ellipse at 40% 90%, var(--wash-blue) 0%, transparent 45%),
      linear-gradient(160deg, var(--wash-blue), var(--wash-lilac) 45%, var(--wash-pink));
    box-shadow:0 6px 24px rgba(120,100,120,.18);
  }
  .frame{position:absolute;pointer-events:none}
  .frame--outer{inset:32px;border:2px solid var(--gold)}
  .frame--inner{inset:42px;border:1.5px solid var(--gold-light)}

  .florals{
    position:absolute;width:150px;height:430px;
    background:linear-gradient(180deg,
      var(--petal-pink) 0%, var(--leaf) 22%, var(--petal-violet) 40%,
      var(--leaf) 58%, var(--petal-pink) 78%, var(--leaf) 100%);
    -webkit-mask-image:radial-gradient(ellipse 50% 50% at 50% 50%, #000 55%, transparent 100%);
            mask-image:radial-gradient(ellipse 50% 50% at 50% 50%, #000 55%, transparent 100%);
    opacity:.55;
  }
  .florals--left{left:-20px;top:400px}
  .florals--right{right:-20px;top:220px}

  .content{position:absolute;inset:0;text-align:center}
  .greeting{
    position:absolute;left:0;right:0;top:150px;
    font-size:24px;line-height:30px;letter-spacing:2px;
  }
  .greeting strong{display:block;font-weight:700;color:var(--gold-deep)}
  .couple{
    position:absolute;left:0;right:0;top:325px;
    font-family:"Great Vibes",cursive;font-weight:400;font-size:112px;line-height:108px;color:var(--gold);
  }
  .couple span{display:block}
  .couple .amp{font-size:100px}
  .venue{position:absolute;left:0;right:0;top:676px;font-size:28px;font-weight:700;letter-spacing:2px;color:var(--gold-deep)}
  .address{position:absolute;left:0;right:0;top:716px;font-size:22px;line-height:28px;letter-spacing:2px}
  .date{position:absolute;left:0;right:0;top:792px;font-size:30px;font-weight:700;letter-spacing:1px;color:var(--gold-deep)}

  .schedule{
    list-style:none;
    position:absolute;left:110px;right:110px;top:880px;
    display:flex;justify-content:space-between;
  }
  .schedule__item{width:110px;display:flex;flex-direction:column;align-items:center;gap:10px;font-size:20px}
  .schedule__item svg{width:56px;height:66px;stroke:var(--gold);fill:none;stroke-width:2.4;stroke-linecap:round;stroke-linejoin:round}
</style>
</head>
<body>
  <article class="invitation">
    <div class="florals florals--left" role="img" aria-label="Watercolour pink and violet flowers with green leaves"></div>
    <div class="florals florals--right" role="img" aria-label="Watercolour pink and violet flowers with green leaves"></div>

    <div class="frame frame--outer"></div>
    <div class="frame frame--inner"></div>

    <div class="content">
      <p class="greeting">
        BU MUTLU GÜNÜMÜZDE<br>
        SİZLERİ DE ARAMIZDA<br>
        GÖRMEKTEN MUTLULUK<br>
        DUYACAĞIZ, DÜĞÜNÜMÜZE
        <strong>DAVETLİSİNİZ</strong>
      </p>

      <h1 class="couple">
        <span>Sena</span>
        <span class="amp">&amp;</span>
        <span>Kaan</span>
      </h1>

      <p class="venue">LAVANTA KORU</p>
      <p class="address">YALIBOYU, ÇINAR SOK. NO:14<br>BEYKOZ, ISTANBUL</p>
      <p class="date">24TH AĞUSTOS, 2024</p>

      <ul class="schedule">
        <li class="schedule__item">
          <svg viewBox="0 0 56 66" aria-label="Karşılama"><path d="M16 6h24l-2 18a10 10 0 0 1-20 0z" fill="var(--gold)"/><path d="M28 34v24M18 60h20"/></svg>
          <span>18:00</span>
        </li>
        <li class="schedule__item">
          <svg viewBox="0 0 56 66" aria-label="Nikah"><circle cx="20" cy="40" r="13"/><circle cx="36" cy="40" r="13"/><path d="M24 14l4-5 4 5-4 4z"/><path d="M18 10l-4-3M38 10l4-3M28 4v-2"/></svg>
          <span>19:00</span>
        </li>
        <li class="schedule__item">
          <svg viewBox="0 0 56 66" aria-label="Yemek"><path d="M12 6v12a5 5 0 0 0 10 0V6M17 6v50"/><ellipse cx="38" cy="16" rx="6" ry="10"/><path d="M38 26l-14 32"/></svg>
          <span>20:00</span>
        </li>
        <li class="schedule__item">
          <svg viewBox="0 0 56 66" aria-label="Sonsuza dek"><path d="M28 40c-6-8-18-8-18 0s12 8 18 0 18-8 18 0-12 8-18 0z"/></svg>
          <span>&nbsp;</span>
        </li>
      </ul>
    </div>
  </article>
</body>
</html>
```